Spirits Bottle Label-Brand Name Reed & Barrow

Design a spirits bottle label per specifications outlined. Label size Front 3.875x 4.5,Back 2x4, topper 1x5.7. Must have established 2020, 40% Alcohol by volume. 40 proof. Sherry Cask Settled. Bottle # 1 of 1320. Caribbean Rum. Trademark logo must be on the label. Back of label has to have all the information outlined in photo. Topper & Front of the label the designer can you his creativity. Color scheme is negotiable and designers can be creative.

Target Market(s)

Adults aged 21 with an appealing appearance that caters to a young professionals and seasoned adults

Font styles to use
Sans Serif

Colors
886aae
33b8a4
33a6d7

Requirements
Must have
• -Reed & Barrow Trademark Logo which is attached.
-Caribbean Rum
-40% Alcohol By Volume
-80 Proof
-Sherry Cask Settled
-Established 2020

```html
<!DOCTYPE html>
<html lang="en">
<head>
<meta charset="utf-8">
<title>Reed &amp; Barrow — Caribbean Rum Label Set</title>
<link rel="stylesheet" href="https://fonts.googleapis.com/css2?family=Cinzel:wght@400;500&family=Cormorant+Garamond:wght@500&family=PT+Sans:wght@400;700&family=Roboto+Condensed:wght@400;700&display=swap">
<style>
  :root {
    --label: #2a2a2a;
    --ink: #ffffff;
    --ink-soft: #d9d9d9;
    --page: #ffffff;
    --panel: #c8c8c8;
    --pill-ink: #1f1f1f;
  }
  html, body { margin: 0; padding: 0; overflow: hidden; }
  body { width: 982px; height: 1200px; background: var(--page); position: relative; }

  .label { position: absolute; background: var(--label); color: var(--ink); border-radius: 5px; }

  /* Topper */
  .topper { left: 702px; top: 51px; width: 66px; height: 627px; }
  .topper__name {
    position: absolute; left: 50%; white-space: nowrap;
    font-family: "Cinzel", serif; font-size: 14px; letter-spacing: 3px;
    transform: translate(-50%, -50%) rotate(-90deg);
  }
  .topper__name--upper { top: 135px; }
  .topper__name--lower { top: 508px; }
  .topper__seal { position: absolute; left: 50%; top: 313px; width: 118px; height: 118px; transform: translateX(-50%); }

  /* Front */
  .front { left: 45px; top: 727px; width: 499px; height: 227px; text-align: center; }
  .front__brand { position: absolute; left: 0; right: 0; top: 24px; margin: 0; font-family: "Cinzel", serif; font-weight: 500; font-size: 40px; letter-spacing: 1px; }
  .front__est { position: absolute; left: 0; right: 0; top: 74px; display: flex; justify-content: center; align-items: center; gap: 8px; font-family: "Cormorant Garamond", serif; font-size: 10px; letter-spacing: 3px; }
  .front__est::before, .front__est::after { content: ""; width: 58px; height: 1px; background: var(--ink); }
  .front__type { position: absolute; left: 0; right: 0; top: 105px; font-family: "Cinzel", serif; font-size: 22px; letter-spacing: 1px; }
  .front__finish { position: absolute; left: 0; right: 0; top: 136px; font-family: "Cormorant Garamond", serif; font-size: 10px; letter-spacing: 3px; color: var(--ink-soft); }
  .front__facts { position: absolute; left: 84px; top: 185px; width: 332px; height: 16px; background: var(--ink); border-radius: 8px; color: var(--pill-ink); font-family: "Cormorant Garamond", serif; font-size: 9.5px; }
  .front__abv { position: absolute; left: 9px; top: 2px; }
  .front__count { position: absolute; right: 9px; top: 2px; }
  .front__proof { position: absolute; left: 50%; top: -13px; width: 40px; height: 40px; transform: translateX(-50%); background: var(--ink); border: 1.5px solid var(--label); border-radius: 50%; box-sizing: border-box; line-height: 1; }
  .front__proof b { display: block; margin-top: 5px; font-weight: 500; font-size: 17px; }
  .front__proof small { display: block; font-size: 7px; letter-spacing: 0.5px; }

  /* Back */
  .back { left: 564px; top: 727px; width: 377px; height: 227px; font-family: "PT Sans", sans-serif; }
  .back__brand { position: absolute; left: 26px; top: 33px; width: 224px; margin: 0; padding-bottom: 8px; border-bottom: 1px solid var(--ink); text-align: center; font-family: "Cinzel", serif; font-weight: 400; font-size: 25px; letter-spacing: 1px; }
  .back__maker { position: absolute; left: 26px; top: 90px; width: 224px; text-align: center; font-size: 12px; line-height: 17px; }
  .back__maker strong { display: block; font-size: 12px; }
  .back__source { position: absolute; left: 307px; top: 20px; width: 66px; text-align: center; font-size: 10.5px; line-height: 13px; }
  .back__panel { position: absolute; left: 307px; top: 79px; width: 66px; height: 143px; background: var(--panel); }
  .back__warning { position: absolute; left: 14px; top: 156px; width: 284px; margin: 0; font-family: "Roboto Condensed", sans-serif; font-size: 8.2px; line-height: 10px; text-align: justify; text-transform: uppercase; }
</style>
</head>
<body>

<section class="label topper" aria-label="Topper label">
  <span class="topper__name topper__name--upper">REED &amp; BARROW</span>
  <svg class="topper__seal" viewBox="0 0 118 118" aria-hidden="true">
    <circle cx="59" cy="59" r="57" fill="#ffffff"/>
  </svg>
  <span class="topper__name topper__name--lower">REED &amp; BARROW</span>
</section>

<section class="label front" aria-label="Front label">
  <h1 class="front__brand">REED &amp; BARROW</h1>
  <div class="front__est">EST. 2020</div>
  <div class="front__type">CARIBBEAN RUM</div>
  <div class="front__finish">SHERRY CASK SETTLED</div>
  <div class="front__facts">
    <span class="front__abv">40% ALC. BY VOL. 750ML</span>
    <span class="front__proof"><b>80</b><small>PROOF</small></span>
    <span class="front__count">Bottle No. 0001 of 1320</span>
  </div>
</section>

<section class="label back" aria-label="Back label">
  <h2 class="back__brand">REED &amp; BARROW</h2>
  <div class="back__maker">distilled and bottled by
    <strong>REED &amp; BARROW DISTILLERY</strong>
    <strong>MILLBROOK, NC 27000</strong>
  </div>
  <p class="back__warning"><b>Government Warning:</b> (1) According to the Surgeon General, women should not drink alcoholic beverages during pregnancy because of the risk of birth defects. (2) Consumption of alcoholic beverages impairs your ability to drive a car or operate machinery, and may cause health problems.</p>
  <div class="back__source">Distilled<br>From<br>Sugar<br>Cane</div>
  <div class="back__panel"></div>
</section>

</body>
</html>
```